IT Consultancy Website Redesign

We would like to redesign our current website.

We have an overall look/feel we like based on a rendering we have for our homepage. (Attached)

Pages that need to be designed (11 total):

-Homepage

-Overview (not it's own page just a navigation header/drop down title)
-About Us
-Why Choose Vorniq
-Our Approach

-Insights (not it's own page just a navigation header/drop down title)
-Insights (Blog)
-Case Studies
-Events

-Services (not it's own page just a navigation header/drop down title)
- Run-State Support

-Industries
-Legal

-Careers
-Contact page

If you have any questions please ask.

Target Market(s)

Meridale 500 C-suite executives

Industry/Entity Type

It Company

Coding

Coded - Design and coding required

Number of Pages Required

5+ page

Font styles to use
Serif
Sans Serif

Requirements
Must have
• Pages must closely resemble the example provided

```html
<!DOCTYPE html>
<html lang="en">
<head>
<meta charset="utf-8">
<title>Vorniq Solutions — IT Strategy and Implementation</title>
<link href="https://fonts.googleapis.com/css2?family=Playfair+Display:wght@700;900&family=Lato:wght@400;700&family=Roboto:wght@400;500&display=swap" rel="stylesheet">
<style>
:root{
  --red:#e3262d;
  --ink:#222222;
  --text:#3a3a3a;
  --muted:#6b6b6b;
  --light:#f4f4f4;
  --dark:#1e1f22;
  --white:#ffffff;
}
*{margin:0;padding:0;box-sizing:border-box}
html,body{width:1200px;height:4672px;overflow:hidden}
body{position:relative;background:var(--white);font-family:'Lato',sans-serif;color:var(--text)}
.abs{position:absolute}
.serif{font-family:'Playfair Display',serif;font-weight:900;color:var(--ink)}
.photo{position:absolute}

/* hero */
.hero{position:absolute;left:0;top:0;width:1200px;height:571px;background:linear-gradient(160deg,#5a5550 0%,#3b3a3a 45%,#252528 100%)}
.brand{position:absolute;font-family:'Lato',sans-serif;font-weight:700;color:var(--white);letter-spacing:1px}
.brand small{display:block;font-size:10px;letter-spacing:6px;font-weight:400}
.topnav{position:absolute;left:556px;top:35px;display:flex;gap:16px;font-size:14px;color:var(--white);font-weight:700}
.btn-outline-light{position:absolute;left:993px;top:26px;width:134px;height:38px;border:1.5px solid #ddd;color:var(--white);font-size:14px;font-weight:700;display:flex;align-items:center;justify-content:center}
.hero-title{position:absolute;left:0;width:1200px;top:208px;text-align:center;font-size:58px;color:var(--white)}
.hero-sub{position:absolute;left:0;width:1200px;top:290px;text-align:center;font-size:21px;color:var(--white)}
.btn{position:absolute;display:flex;align-items:center;justify-content:center;font-size:13px;font-weight:700}
.btn-red{background:var(--red);color:var(--white)}
.btn-ghost{border:1.5px solid #ddd;color:var(--white)}

/* intro */
.intro-title{left:87px;top:664px;font-size:46px;line-height:52px}
.intro-text{left:92px;top:782px;width:500px;font-size:20px;line-height:26px}
.feature{position:absolute;left:143px;width:400px}
.feature h3{font-family:'Playfair Display',serif;font-weight:900;font-size:20px;color:var(--ink);letter-spacing:.5px;line-height:24px}
.feature p{font-size:16px;line-height:22px;margin-top:8px;color:var(--text)}
.feature-bullet{position:absolute;left:93px;width:12px;height:12px;background:var(--red)}
.quote{left:712px;top:1240px;width:400px;font-size:20px;font-style:italic;line-height:26px;color:var(--text)}
.quote-by{left:712px;top:1298px;font-family:'Playfair Display',serif;color:var(--red);font-size:16px}

/* help */
.help{position:absolute;left:0;top:1392px;width:1200px;height:689px;background:var(--light)}
.section-title{position:absolute;left:0;width:1200px;text-align:center;font-size:42px}
.service-card{position:absolute;top:1572px;width:300px;height:428px}
.service-card h4{position:absolute;left:22px;top:168px;font-family:'Playfair Display',serif;font-weight:900;font-size:20px;color:var(--white)}
.service-card .rule{position:absolute;left:22px;top:202px;width:138px;height:2px;background:var(--white)}
.service-card p{position:absolute;left:22px;top:205px;width:270px;font-size:15px;line-height:22px;color:var(--white)}
.service-card .more{position:absolute;left:22px;top:300px;font-size:13px;font-weight:700;color:var(--white)}

/* featured */
.proj-title{left:633px;top:2170px;font-size:44px}
.proj-sub{left:633px;top:2252px;font-family:'Roboto',sans-serif;font-weight:400;font-size:30px;color:var(--ink)}
.proj-text{left:633px;top:2300px;width:490px;font-size:20px;line-height:26px}
.btn-outline-red{border:2px solid var(--red);color:var(--red);background:var(--white)}
.dot{position:absolute;top:2546px;width:11px;height:11px;border-radius:50%;border:1.5px solid var(--ink)}

/* industries */
.industry{position:absolute;top:2810px;width:248px;height:310px}
.industry-label{position:absolute;top:3140px;width:248px;text-align:center;font-family:'Roboto',sans-serif;font-size:26px;color:var(--ink)}
.industry-rule{position:absolute;top:3182px;width:30px;height:3px;background:var(--red)}

/* blogs */
.blogs{position:absolute;left:0;top:3245px;width:1200px;height:581px;background:var(--light)}
.blog-photo{position:absolute;top:3427px;width:300px;height:232px}
.blog-title{position:absolute;top:3684px;width:300px;font-family:'Roboto',sans-serif;font-size:21px;line-height:26px;color:var(--ink)}
.blog-meta{position:absolute;top:3744px;font-size:12px;color:var(--muted)}

/* join */
.join{position:absolute;left:0;top:3826px;width:1200px;height:426px;background:linear-gradient(100deg,#3e3c3b 0%,#5b5754 50%,#2a2b2e 100%)}
.join-title{position:absolute;left:299px;top:3900px;font-size:44px;color:var(--white)}
.join-text{position:absolute;left:299px;top:3972px;width:460px;font-size:20px;line-height:26px;color:var(--white)}

/* footer */
.footer{position:absolute;left:0;top:4252px;width:1200px;height:420px;background:var(--dark)}
.footnav{position:absolute;left:518px;top:4318px;display:flex;gap:21px;font-family:'Roboto',sans-serif;font-size:21px;color:var(--white)}
.contact{position:absolute;top:4430px;font-family:'Roboto',sans-serif;font-size:21px;line-height:31px;color:var(--white)}
.foot-line{position:absolute;left:0;top:4605px;width:1200px;height:1px;background:#55575c}
.foot-small{position:absolute;top:4632px;font-size:14px;color:#c8c8c8}
</style>
</head>
<body>

<!-- hero -->
<section class="hero" role="img" aria-label="Team of IT consultants working together at computers in an office"></section>
<div class="brand" style="left:69px;top:22px;font-size:30px">VORNIQ<small>SOLUTIONS</small></div>
<nav class="topnav"><span>Over view</span><span>Our Focus</span><span>Industries</span><span>Insights</span><span>Careers</span></nav>
<div class="btn-outline-light">Contact Us</div>
<h1 class="serif hero-title">IT Strategy and Implementation</h1>
<p class="hero-sub">We take your company to the cutting edge of efficiency</p>
<div class="btn btn-red" style="left:435px;top:359px;width:151px;height:42px">Learn More</div>
<div class="btn btn-ghost" style="left:611px;top:359px;width:151px;height:42px">Get in Touch</div>

<!-- intro -->
<h2 class="abs serif intro-title">Impower Digitial<br>Transformation</h2>
<p class="abs intro-text">Vorniq Solutions is a team of IT experts who command the IT field and its related software. From consultancy to implementation, we can help you identify the best solutions for your company and see them through to smooth, constant, and long-lasting operation.</p>

<div class="feature-bullet" style="top:972px"></div>
<div class="feature" style="top:958px"><h3>EXPERIENCED SOLUTION FOCUSED DEVELOPERS</h3><p>All of our developers have vast experience in the FlowDesk environment.</p></div>
<div class="feature-bullet" style="top:1098px"></div>
<div class="feature" style="top:1092px"><h3>SUPERIOR SERVICE</h3><p>Our customers come first and our client retention rate of 98% proves it.</p></div>
<div class="feature-bullet" style="top:1214px"></div>
<div class="feature" style="top:1208px"><h3>COMPETITIVE PRICING</h3><p>All solutions are presented with several delivery options e.g full-time US developers, a hybrid of US + near shore, or all near shore.</p></div>

<div class="photo" style="left:714px;top:685px;width:390px;height:532px;background:linear-gradient(160deg,#d9d6d2,#8f8c89 60%,#bdb6ad)" role="img" aria-label="Consultants reviewing work together on a laptop"></div>
<p class="abs quote">“Vorniq solution has developed much faster Solutions for us.We highly Recommand”</p>
<p class="abs quote-by">-Lena Marsh,CEO Quorvex</p>

<!-- help -->
<section class="help"></section>
<h2 class="section-title serif" style="top:1456px">Here’s How We Help You</h2>

<div class="service-card" style="left:72px;background:linear-gradient(160deg,#8a8682,#4e4b49 70%,#3a3836)" role="img" aria-label="Developer working at a laptop"><h4>Managed Services</h4><div class="rule"></div></div>
<div class="service-card" style="left:450px;background:linear-gradient(160deg,#4b4f56,#6f7174 55%,#9a9793)" role="img" aria-label="Code on a monitor above hands on a keyboard"><h4>Implementation Services</h4><div class="rule"></div></div>
<div class="service-card" style="left:827px;background:linear-gradient(180deg,#8d8680 0%,#b9555a 50%,#e3262d 100%)" role="img" aria-label="Support agent wearing a headset">
  <h4>Virtual Assistance</h4>
  <p>we can help you gain back business momentum and ensure your team has all the FlowDesk support you need to achieve your goals.</p>
  <span class="more">Read More</span>
  <div class="rule" style="top:320px"></div>
</div>

<!-- featured -->
<div class="photo" style="left:0;top:2081px;width:557px;height:548px;background:linear-gradient(150deg,#d8d5d0,#b9b2a8 50%,#8c8680)" role="img" aria-label="Doctor writing notes beside a tablet"></div>
<h2 class="abs serif proj-title">Featured Projects</h2>
<h3 class="abs proj-sub">Halden Hospital IT Project</h3>
<p class="abs proj-text">Halden hospital wanted the flowdesk project implemented in there system.We as a team observed the current system of the hospital and it’s needs and our team implemented the system,They now run a success flowdesk system .</p>
<div class="btn btn-outline-red" style="left:633px;top:2460px;width:186px;height:46px">View Details</div>
<div class="dot" style="left:633px;background:var(--ink)"></div>
<div class="dot" style="left:656px"></div>
<div class="dot" style="left:679px"></div>

<!-- industries -->
<h2 class="section-title serif" style="top:2696px">Industries</h2>
<div class="industry" style="left:69px;background:linear-gradient(160deg,#6a6764,#3f3d3b 60%,#a66a3c)" role="img" aria-label="Lawyer holding a gavel"></div>
<div class="industry" style="left:343px;background:linear-gradient(160deg,#e8e8ea,#c9c4c0 60%,#9fb6c6)" role="img" aria-label="Healthcare workers with a tablet"></div>
<div class="industry" style="left:609px;background:linear-gradient(160deg,#4a4643,#c77d31 55%,#6b6f72)" role="img" aria-label="Factory workers in safety gear with a laptop"></div>
<div class="industry" style="left:881px;background:linear-gradient(160deg,#3f4756,#e3e3e5 50%,#bdbdbd)" role="img" aria-label="Professional reading a tablet"></div>
<p class="industry-label" style="left:69px">Legal</p><div class="industry-rule" style="left:178px"></div>
<p class="industry-label" style="left:343px">Healthcare</p><div class="industry-rule" style="left:452px"></div>
<p class="industry-label" style="left:609px">Manufactoring</p><div class="industry-rule" style="left:718px"></div>
<p class="industry-label" style="left:872px;top:3136px">Utilities</p><div class="industry-rule" style="left:982px;top:3180px"></div>

<!-- blogs -->
<section class="blogs"></section>
<h2 class="section-title serif" style="top:3310px">Blogs</h2>
<div class="blog-photo" style="left:71px;background:linear-gradient(160deg,#cfd3d6,#5b5f66 60%,#2e3035)" role="img" aria-label="Team meeting around laptops"></div>
<div class="blog-photo" style="left:449px;background:linear-gradient(160deg,#eef0f2,#c9d4de 50%,#7b7f85)" role="img" aria-label="Presenter sketching a diagram on a whiteboard"></div>
<div class="blog-photo" style="left:828px;background:linear-gradient(160deg,#e9eaec,#b8bcc2 50%,#4a4c52)" role="img" aria-label="Workshop in a bright meeting room"></div>
<p class="blog-title" style="left:70px">Highlights from FlowDesk’s Aldon realease</p>
<p class="blog-title" style="left:447px">How FlowDesk Uses Its Own HR Platform</p>
<p class="blog-title" style="left:825px">How Carrow Financial Benefits from FlowDesk</p>
<p class="blog-meta" style="left:70px">Mara Ellis &nbsp;|&nbsp; 23,May 2020</p>
<p class="blog-meta" style="left:447px">Mara Ellis &nbsp;|&nbsp; 12,May 2020</p>
<p class="blog-meta" style="left:825px">Mara Ellis &nbsp;|&nbsp; 15,April 2020</p>

<!-- join -->
<section class="join" role="img" aria-label="Developer writing code on a laptop"></section>
<h2 class="serif join-title">Join Vorniq</h2>
<p class="join-text">We are always looking to add bright and telented people to our flowDesk&nbsp; focused team for Available opportunities.</p>
<div class="btn btn-red" style="left:299px;top:4068px;width:158px;height:38px">Join Now</div>

<!-- footer -->
<footer class="footer"></footer>
<div class="brand" style="left:73px;top:4300px;font-size:40px">VORNIQ<small style="font-size:13px;letter-spacing:9px">SOLUTIONS</small></div>
<nav class="footnav"><span>News</span><span>Overview</span><span>Careers</span><span>Services</span><span>Contact</span><span>Our Partners</span></nav>

<svg class="abs" style="left:70px;top:4430px" width="32" height="32" viewBox="0 0 32 32"><circle cx="16" cy="16" r="16" fill="#d8d8d8"/><path d="M11 8 C9 9 8 11 9 14 C11 19 14 22 19 24 C22 25 24 23 25 21 L21 18 L19 20 C16 19 14 17 13 14 L15 12 Z" fill="#1e1f22"/></svg>
<p class="contact" style="left:120px">Phone Number<br>555.014.2290</p>
<svg class="abs" style="left:430px;top:4436px" width="32" height="32" viewBox="0 0 32 32"><circle cx="16" cy="16" r="16" fill="#d8d8d8"/><rect x="8" y="11" width="16" height="11" fill="none" stroke="#1e1f22" stroke-width="2"/><path d="M8 11 L16 17 L24 11" fill="none" stroke="#1e1f22" stroke-width="2"/></svg>
<p class="contact" style="left:480px;top:4436px">Email<br>info@vorniqsolutions.com</p>
<svg class="abs" style="left:788px;top:4432px" width="32" height="32" viewBox="0 0 32 32"><circle cx="16" cy="16" r="16" fill="#d8d8d8"/><path d="M16 7 C12 7 10 10 10 13 C10 17 16 25 16 25 C16 25 22 17 22 13 C22 10 20 7 16 7 Z" fill="#1e1f22"/><circle cx="16" cy="13" r="2.5" fill="#d8d8d8"/></svg>
<p class="contact" style="left:836px;top:4432px">Address<br>4180 Larkspur Ave Suite 12<br>Brookfield, VA 23000</p>

<div class="foot-line"></div>
<p class="foot-small" style="left:73px">© 2020 All Rights Reserved</p>
<svg class="abs" style="left:560px;top:4624px" width="30" height="30" viewBox="0 0 30 30"><rect x="1" y="1" width="28" height="28" fill="none" stroke="#e3262d" stroke-width="2"/><path d="M9 18 L15 12 L21 18" fill="none" stroke="#ffffff" stroke-width="2"/></svg>
<p class="foot-small" style="left:958px">© 2020 Vorniqsolutions</p>

</body>
</html>
```